Pagecraft website build: Quirk literary annual (initial design work supplied)

Our brand guidelines provide the look and feel for the website - we just need someone to create it based on our mock ups!
PLEASE NOTE:
- Please base our website off the website pages within the brief (ie homepage is GREEN)
- please ensure each page will be standalone (not a scrolling home page)
- please only use filtered duotone style photography as a hold, if you think the page needs a photo.
-please not the websites i have provided as an influence - especially TIDE YEARLY. We want very little photography.

Quirk is a literary and arts journal that provides a platform for both emerging and established writers and artists from New Zealand and beyond. We are passionate about sharing insights into the intimate and unique worlds of creatives with short stories, poetry, and art – showcasing raw and unfiltered glimpses into their world.

We have our brand guidelines and logo finalised, with a 'look and feel' design for the website within our attached brand guidelines document. We just need someone to design this simple website on Pagecraft for us. It will have five pages and will need a newsletter sign up link:
Home page
About us page
Submissions page
Purchase page
Contact page

DRAFT WEB COPY

ABOUT
QUIRK is an independent literary annual journal established in 2022 by Hazel Wintergate and Mereana Clift that publishes unrepentant unfiltered accounts of life, eclectic takes on the mundane ordinary, and deep dives into modern love & sexuality.
Founder, Editor: Hazel Arohanui Wintergate
Founder, Production Director: Mereana Clift
Art Direction: Lorna Pike
Editorial Assistant: Kirsten Holloway-Dunn

I suggest duotone fashion-esque photography which is very Vesna Kordell/ Palm Springs vibe but not obviously identifiable.
· I love the style of Rufus Tennick for our shoot in particular. Group lazing around a pool, leisurely, glam, but effortless and ironically looking very natural – as though – yes, these are our lives.
SUBMISSION PAGE
Quirk welcomes submissions all year round.
We are drawn to dark humour, satirical takes on the social scene, and starkly honest accounts of ordinary life. Diversity is celebrated, adversity is welcomed and, above all, personal expression is championed. We are particularly seeking content that takes risks, screams of honesty and celebrates life’s most extraordinary moments.
Selected works will be published in our annual publication.

Submission guidelines
We accept flash fiction, short stories and poetry. Individual entries not to mustn’t exceed 2000 words.
Submitted work must be unpublished and in English. We welcome simultaneous submissions, but must be notified immediately if your manuscript is accepted for publication elsewhere or appears in any print or online source. We will endeavour to respond to all submissions within four weeks.
Please send submissions as a word document along with a brief bio of 50 words to pages@quirkjournal.test
PO Box[EB2]
​Note on Copyright: Copyright remains with the author.

Annual short story competition
Volume Alpha is interested in all that is spiritual, coincidental, or mysterious. Stories selected for this issue reflect life’s uncanny moments, those that defy explanation, and experiences that promote personal and spiritual growth. Entires must be no longer than 2000 words.

First prize: 1000
Second prize: 500
Third prize: 200[EB3]

SUPPORT US
Since our launch in 2022, we have relied upon the generous support of our creative business community in Wellington City, New Zealand. If you read us, or love our ethos, please consider a donation.
Link to chipinhere page
Updates

Hello designers
I would ideally love to have someone turn this around within a few weeks, because the design work has mostly been provided.
Thanks
Hazel

Hi everyone Please ensure you read our brand guidelines and follow the brief. Please note we do not yet have a product, as this is a new venture, so there is no point including images of a magazine that doesn't yet exist. Some further comment to ensure we get there: - We want all pages to be separate pages (not a scrolling home page) with a different colour based on the guidelines - The home page must look just as it does in the brand guidelines - There is no archive page (please read brief) as we have no archive yet. The pages are: Home, About, Contact, Competitions and submissions Thank you

Target Market(s)

writers and creatives

Industry/Entity Type

Writing/ creative/ publishing

Coding

Coded - Design and coding required

Number of Pages Required

4 page

Font styles to use
Other font styles liked:
• COTTA and Univers - as per brand guidelines

Requirements
Must have
• Pagecraft designer needed to design our mocked up webpages.
Nice to have
• As close to the brand guideline mock ups as possible (see page 11,12,13)
Should not have
• anything outside of the brand guidelines

```html
<!DOCTYPE html>
<html lang="en">
<head>
<meta charset="utf-8">
<title>Quirk — literary annual</title>
<link href="https://fonts.googleapis.com/css2?family=Bellefair&family=Oswald:wght@300;400&family=Figtree:wght@400;700&display=swap" rel="stylesheet">
<style>
:root{
  --blush:#fdf0f4;
  --rose:#b9566f;
  --berry:#bd4670;
  --plum:#6b3a66;
  --ink:#2b2230;
  --nav:#7b3f6b;
  --lilac:#e5d2f0;
  --gold:#c9a84b;
  --white:#ffffff;
  --grey:#6f6a70;
}
*{margin:0;padding:0;box-sizing:border-box}
html,body{width:1200px;height:3136px;overflow:hidden;background:var(--white)}
body{position:relative;font-family:'Figtree',sans-serif;color:var(--ink)}
.abs{position:absolute}
.serif{font-family:'Bellefair',serif;font-weight:400}
.wordmark{font-family:'Bellefair',serif;color:var(--berry);line-height:1}

.hero{left:0;top:0;width:1200px;height:573px;background:var(--blush)}
.hero-mark{left:85px;top:18px;font-size:92px}
.nav{right:270px;top:58px;height:22px;display:flex;justify-content:flex-end;align-items:center;font-family:'Oswald',sans-serif;font-weight:300;font-size:16px;line-height:1;color:var(--nav);text-transform:uppercase;white-space:nowrap}
.nav span{padding:0 16px}
.nav span:first-child{padding-left:0}
.nav span:last-child{padding-right:0}
.nav .sep{display:block;width:1px;height:15px;background:var(--nav)}
.btn{display:flex;align-items:center;justify-content:center;border-radius:30px;font-family:'Oswald',sans-serif;text-transform:uppercase;white-space:nowrap}
.btn-subscribe{left:974px;top:43px;width:140px;height:53px;border:1.5px solid var(--nav);color:var(--nav);font-size:21px}
.hero-title{left:85px;top:210px;width:600px;font-size:49px;line-height:53px;color:var(--ink)}
.hero-lede{left:85px;top:386px;font-size:17px;color:var(--ink)}
.btn-donate{left:85px;top:428px;width:140px;height:53px;border:1.5px solid var(--berry);color:var(--berry);font-size:21px}

.about-title{left:85px;top:680px;font-size:48px;color:var(--plum)}
.about-copy{left:85px;top:756px;width:520px;font-size:18px;line-height:25.5px;color:#3b3440}
.credits{left:746px;top:756px;font-size:18px;line-height:25.5px}
.credits div{margin-bottom:19px}

.band{left:0;top:1028px;width:1200px;height:404px;background:var(--rose)}
.band-title{left:85px;top:1130px;font-size:48px;color:var(--white)}
.band-copy{left:85px;top:1203px;font-size:20px;color:var(--white)}

.card{top:1269px;width:237px;height:325px;box-shadow:0 8px 18px rgba(0,0,0,.12);overflow:hidden}
.card .tag{position:absolute;top:44px;font-family:'Oswald',sans-serif;font-weight:300;font-size:12px;text-transform:uppercase;white-space:nowrap}
.card .tag.l{left:18px}.card .tag.r{right:18px}
.card .mark{position:absolute;left:0;width:100%;top:24px;text-align:center;font-family:'Bellefair',serif;font-size:42px;line-height:1}
.card svg{position:absolute;left:12px;top:92px}
.info{top:1622px;width:237px;text-align:center}
.info h3{font-family:'Oswald',sans-serif;font-weight:400;font-size:21px;text-transform:uppercase;color:var(--ink);white-space:nowrap}
.info p{margin-top:12px;font-size:17px;line-height:24.5px;color:var(--grey)}
.btn-dl{margin:22px auto 0;width:130px;height:42px;border:1.5px solid var(--ink);color:var(--ink);font-size:13px}

.support-title{left:0;top:1905px;width:1200px;text-align:center;font-size:48px;color:var(--plum)}
.support-copy{left:231px;top:1984px;width:738px;text-align:center;font-size:18px;line-height:25.5px;color:#3b3440}
.btn-give{left:529px;top:2089px;width:141px;height:53px;border:1.5px solid var(--berry);color:var(--berry);font-size:21px}

.news{left:0;top:2260px;width:1200px;height:466px;background:linear-gradient(100deg,#ead8f3 0%,#e3cdef 60%,#dcc4ec 100%)}
.news .sprigs{position:absolute;right:0;top:0;width:440px;height:466px;background:radial-gradient(ellipse at 60% 55%,rgba(190,90,210,.55),rgba(190,90,210,0) 65%),linear-gradient(160deg,rgba(0,0,0,0) 60%,rgba(170,220,240,.55) 100%)}
.news-title{left:0;top:2372px;width:1200px;text-align:center;font-size:48px;line-height:53px;color:var(--plum)}
.news-field{left:389px;top:2506px;width:265px;height:50px;background:var(--white);font-size:13px;color:#8a8590;padding:18px 0 0 17px}
.btn-news{left:672px;top:2506px;width:138px;height:50px;background:var(--plum);color:var(--white);font-size:21px}
.news-privacy{left:0;top:2593px;width:1200px;text-align:center;font-size:15px;color:#3b3440}

.foot h4{font-family:'Bellefair',serif;font-weight:400;font-size:25px;color:var(--ink)}
.foot .col1{left:86px;top:2846px;width:340px}
.foot .col1 p{margin-top:20px;font-size:15px;line-height:22.5px;color:var(--grey)}
.foot .give{left:86px;top:3030px;font-family:'Oswald',sans-serif;font-size:19px;text-transform:uppercase;display:flex;align-items:center;gap:12px;color:var(--ink)}
.foot .menu{left:562px;top:2848px}
.foot .social{left:777px;top:2848px}
.foot ul{list-style:none;margin-top:22px}
.foot li{font-size:15px;line-height:38px;color:var(--grey)}
.foot .social li{color:var(--plum);text-decoration:underline}
.foot .wordmark{left:958px;top:2836px;font-size:92px}
.foot .made{left:943px;top:2950px;font-size:15px}
.foot .made span{color:var(--berry);text-decoration:underline}
</style>
</head>
<body>

<header class="hero abs"></header>
<div class="wordmark hero-mark abs">quirk</div>
<nav class="nav abs"><span>Home</span><i class="sep"></i><span>About us</span><i class="sep"></i><span>Submissions</span><i class="sep"></i><span>Purchase</span><i class="sep"></i><span>Contact</span></nav>
<div class="btn btn-subscribe abs">Subscribe</div>
<h1 class="serif hero-title abs">Quirk is a plucky little pubication out of Wellington, New Zealand</h1>
<p class="hero-lede abs">QUIRK is an independent literary annual journal established in 2022</p>
<div class="btn btn-donate abs">Donate us</div>
<svg class="abs" style="left:731px;top:167px" width="383" height="406" viewBox="0 0 383 406">
  <path d="M1 406 V44 H20 V26 M363 26 V44 H382 V406" fill="none" stroke="#d98aa6" stroke-width="1.5"/>
  <path d="M20 26 H40 V2 H343 V26 H363" fill="none" stroke="#d98aa6" stroke-width="1.5"/>
  <rect x="12" y="16" width="12" height="12" fill="none" stroke="#d98aa6" stroke-width="1.5"/>
  <rect x="359" y="16" width="12" height="12" fill="none" stroke="#d98aa6" stroke-width="1.5"/>
  <defs><linearGradient id="heroTone" x1="0" y1="0" x2="0" y2="1"><stop offset="0" stop-color="#b83c66"/><stop offset="0.55" stop-color="#d75a82"/><stop offset="1" stop-color="#c84a74"/></linearGradient></defs>
  <path role="img" aria-label="Duotone photo of a long arched corridor with steps" d="M16 406 V56 H59 V17 H327 V56 H368 V406 Z" fill="url(#heroTone)"/>
</svg>

<section class="about">
  <h2 class="serif about-title abs">About Quirk</h2>
  <p class="about-copy abs">QUIRK is an independent literary annual journal established in 2022 by Hazel Wintergate and Mereana Clift that publishes unrepentant unfiltered accounts of life, eclectic takes on the mundane ordinary, and deep dives into modern love &amp; sexuality.</p>
  <div class="credits abs">
    <div><b>Founder, Editor</b>: Hazel Arohanui Wintergate</div>
    <div><b>Founder, Production Director</b>: Mereana Clift</div>
    <div><b>Art Direction</b>: Lorna Pike</div>
    <div><b>Editorial Assistant</b>: Kirsten Holloway-Dunn</div>
  </div>
</section>

<section class="band abs"></section>
<h2 class="serif band-title abs">Our Upcoming Magazine</h2>
<p class="band-copy abs">Our back catalogue is available in digital format for a reduced price.</p>

<div class="card abs" style="left:85px;background:#f3ebe0;color:#6f7326">
  <span class="tag l">Issue 001</span><span class="mark">quirk</span><span class="tag r">Aug 2022</span>
  <svg width="213" height="233" viewBox="0 0 213 233"><path d="M2 233 V20 H14 V10 H199 V20 H211 V233" fill="none" stroke="#c9a84b"/><path role="img" aria-label="Olive duotone portrait photo" d="M10 233 V30 H32 V8 H181 V30 H203 V233 Z" fill="#8e8a2e"/></svg>
</div>
<div class="card abs" style="left:348px;background:#b9566f;color:#fff">
  <span class="tag l">Issue 002</span><span class="mark">quirk</span><span class="tag r">Sep 2022</span>
  <svg width="213" height="233" viewBox="0 0 213 233"><path d="M2 233 V20 H14 V10 H199 V20 H211 V233" fill="none" stroke="#c9a84b"/><path role="img" aria-label="Berry duotone photo of angular architecture" d="M10 233 V30 H32 V8 H181 V30 H203 V233 Z" fill="#8c3763"/></svg>
</div>
<div class="card abs" style="left:613px;background:#fff;color:#b9566f">
  <span class="tag l" style="color:#555">Issue 003</span><span class="mark">quirk</span><span class="tag r" style="color:#555">Oct 2022</span>
  <svg width="213" height="233" viewBox="0 0 213 233"><path d="M2 233 V20 H14 V10 H199 V20 H211 V233" fill="none" stroke="#c9a84b"/><defs><linearGradient id="leaf" x1="0" y1="0" x2="1" y2="1"><stop offset="0" stop-color="#2f3a2a"/><stop offset="0.5" stop-color="#5a45b0"/><stop offset="1" stop-color="#9a4fb3"/></linearGradient></defs><path role="img" aria-label="Blue and violet duotone photo of a large leaf" d="M10 233 V30 H32 V8 H181 V30 H203 V233 Z" fill="url(#leaf)"/></svg>
</div>
<div class="card abs" style="left:876px;background:#6b7b2a;color:#c9a84b">
  <span class="tag l" style="color:#fff">Issue 004</span><span class="mark">quirk</span><span class="tag r" style="color:#fff">Nov 2022</span>
  <svg width="213" height="233" viewBox="0 0 213 233"><path d="M2 233 V20 H14 V10 H199 V20 H211 V233" fill="none" stroke="#c9a84b"/><defs><linearGradient id="pinkPortrait" x1="0" y1="0" x2="1" y2="1"><stop offset="0" stop-color="#e96bb4"/><stop offset="1" stop-color="#7b3a8c"/></linearGradient></defs><path role="img" aria-label="Pink duotone portrait photo" d="M10 233 V30 H32 V8 H181 V30 H203 V233 Z" fill="url(#pinkPortrait)"/></svg>
</div>
<div class="card abs" style="left:1143px;background:#fff;color:#6b3a66">
  <span class="tag l" style="color:#555">Issue 005</span>
  <svg width="213" height="233" viewBox="0 0 213 233"><path d="M2 233 V20 H14 V10 H199 V20 H211 V233" fill="none" stroke="#c9a84b"/><path role="img" aria-label="Violet duotone photo" d="M10 233 V30 H32 V8 H181 V30 H203 V233 Z" fill="#6b4f9a"/></svg>
</div>

<div class="info abs" style="left:85px"><h3>Issue 001 — Aug 2022</h3><p>Lorem ipsum dolor sit amet, consectetur adipiscing elit. Aenean dapibus</p><div class="btn btn-dl">Download now</div></div>
<div class="info abs" style="left:348px"><h3>Issue 002 — Sep 2022</h3><p>Lorem ipsum dolor sit amet, consectetur adipiscing elit. Aenean dapibus</p><div class="btn btn-dl">Download now</div></div>
<div class="info abs" style="left:613px"><h3>Issue 003 — Oct 2022</h3><p>Lorem ipsum dolor sit amet, consectetur adipiscing elit. Aenean dapibus</p><div class="btn btn-dl">Download now</div></div>
<div class="info abs" style="left:876px"><h3>Issue 004 — Nov 2022</h3><p>Lorem ipsum dolor sit amet, consectetur adipiscing elit. Aenean dapibus</p><div class="btn btn-dl">Download now</div></div>
<div class="info abs" style="left:1143px"><h3>Issue 005 — Dec 2022</h3><p>Lorem ipsum dolor sit amet, consectetur adipiscing elit. Aenean dapibus</p><div class="btn btn-dl">Download now</div></div>

<section class="support">
  <h2 class="serif support-title abs">Support Us</h2>
  <p class="support-copy abs">Since our launch in 2022, we have relied upon the generous support of our creative business community in Wellington City, New Zealand. If you read us, or love our ethos, please consider a donation.</p>
  <div class="btn btn-give abs">Give a little</div>
</section>

<section class="news abs"><div class="sprigs" role="img" aria-label="Photo of lilac flower sprigs on a pastel background"></div></section>
<h2 class="serif news-title abs">Subscribe to our weekly<br>newsletter</h2>
<div class="news-field abs">Email Address</div>
<div class="btn btn-news abs">Subscribe</div>
<p class="news-privacy abs">We respect your privacy.</p>

<footer class="foot">
  <div class="col1 abs"><h4>Support Us</h4><p>Since our launch in 2022, we have relied upon the generous support of our creative business community in Wellington City, New Zealand. If you read us, or love our ethos, please consider a donation.</p></div>
  <div class="give abs">Give a little <svg width="22" height="12" viewBox="0 0 22 12"><path d="M0 6 H20 M15 1 L20 6 L15 11" fill="none" stroke="#2b2230" stroke-width="1.5"/></svg></div>
  <div class="menu abs"><h4>Main Menu</h4><ul><li>Home</li><li>About</li><li>Submissions</li><li>Purchase</li><li>Contact</li></ul></div>
  <div class="social abs"><h4>Social</h4><ul><li>Circlepost</li><li>Snapgrid</li><li>Chirpline</li></ul></div>
  <div class="wordmark abs">quirk</div>
  <div class="made abs">Made with <span>Pagecraft</span></div>
</footer>

</body>
</html>
```